Talent Management Company Needs Business Cards

Using one of the logos provided (attached) K&R Talent Collective needs a business card designed.
Please visit our website for more information about us-

www.krtalentcollective.example

The face should feature a dramatic presentation of the logo with the back being reserved for our professional information which is:

The information should be:
Dorian T. Vickers
C.E.O
Email: dtvickers@krtalentcollective.example
Mobile: 555-804-2917
Website: www.krtalentcollective.example

Marcus L. Vickers
Director of Public Relations
Email: mlvickers@krtalentcollective.example
Mobile: 555-806-3350

Jules R. Hampton
Director of Client Development
Email: jhampton@krtalentcollective.example

Simon Hurlock
Director of Brand Development
Email: shurlock@krtalentcollective.example

Would like the logo to have color. I would like to see one side red or black and the other side white but if it looks better in either black or red that would be fine to but would like to see how it comes out.

Please feel free to message me and if you would like just the icon alone I have other image files that I can send as well.

Target Market(s)

Professional Athletes, coaches, entertainers age 18-35 but also must be accepted in the business community

Industry/Entity Type

Business

Requirements
Must have
• 1) Use the logo
2) Double sided
3) Distinctive
Nice to have
• Small simple images for telephone, e-mail, and Url.

```html
<!DOCTYPE html>
<html lang="en">
<head>
<meta charset="utf-8">
<title>K&amp;R Talent Collective — Business Card</title>
<link rel="stylesheet" href="https://fonts.googleapis.com/css2?family=Archivo+Black&family=PT+Sans+Narrow:wght@400;700&display=swap">
<style>
  :root {
    --page: #ffffff;
    --card-light: #c4c4c4;
    --card-mid: #8e8e8e;
    --card-dark: #4a4a4a;
    --brand-red: #c8151b;
    --ink: #151515;
    --shadow: rgba(0, 0, 0, 0.55);
  }
  * { margin: 0; padding: 0; box-sizing: border-box; }
  html, body {
    width: 1200px;
    height: 471px;
    overflow: hidden;
    background: var(--page);
  }
  .sheet {
    position: relative;
    width: 1200px;
    height: 471px;
  }
  .card {
    position: absolute;
    top: 0;
    height: 471px;
    overflow: hidden;
    background: radial-gradient(ellipse 70% 75% at 50% 48%, var(--card-light) 0%, var(--card-mid) 55%, var(--card-dark) 100%);
  }
  .card--front { left: 0; width: 585px; }
  .card--back {
    left: 612px;
    width: 588px;
    background: radial-gradient(ellipse 75% 70% at 42% 40%, var(--card-light) 0%, var(--card-mid) 55%, var(--card-dark) 100%);
  }

  /* front: brand lockup */
  .brand {
    position: absolute;
    left: 0;
    right: 0;
    top: 108px;
    display: flex;
    flex-direction: column;
    align-items: center;
    gap: 28px;
  }
  .brand__circle {
    width: 180px;
    height: 180px;
    border-radius: 50%;
    background: var(--brand-red);
  }
  .brand__name {
    font-family: "PT Sans Narrow", sans-serif;
    font-weight: 400;
    font-size: 44px;
    line-height: 1;
    letter-spacing: 0.5px;
    color: var(--ink);
    text-transform: uppercase;
    white-space: nowrap;
  }

  /* back: identity */
  .identity {
    position: absolute;
    left: 0;
    right: 0;
    top: 62px;
    text-align: center;
    color: var(--brand-red);
    font-family: "Archivo Black", sans-serif;
    text-shadow: 3px 3px 4px var(--shadow);
  }
  .identity__name { font-size: 38px; line-height: 1; }
  .identity__title { font-size: 36px; line-height: 1.1; margin-top: 6px; }

  /* back: contact list */
  .contacts {
    position: absolute;
    left: 0;
    right: 0;
    top: 308px;
    list-style: none;
    display: flex;
    flex-direction: column;
    align-items: center;
    gap: 8px;
  }
  .contact {
    display: flex;
    align-items: center;
    gap: 8px;
    font-family: "PT Sans Narrow", sans-serif;
    font-weight: 700;
    font-size: 27px;
    line-height: 1.2;
    color: var(--ink);
    text-shadow: 1px 1px 2px rgba(255, 255, 255, 0.25);
    white-space: nowrap;
  }
  .contact__icon { flex: none; display: block; }
</style>
</head>
<body>
<main class="sheet">

  <section class="card card--front" aria-label="Card front">
    <div class="brand">
      <span class="brand__circle" aria-hidden="true"></span>
      <span class="brand__name">K&amp;R Talent Collective</span>
    </div>
  </section>

  <section class="card card--back" aria-label="Card back">
    <header class="identity">
      <h1 class="identity__name">Dorian T. Vickers</h1>
      <p class="identity__title">C.E.O</p>
    </header>

    <ul class="contacts">
      <li class="contact contact--email">
        <svg class="contact__icon" width="42" height="28" viewBox="0 0 42 28" aria-hidden="true">
          <rect x="10" y="3" width="30" height="22" rx="2" fill="var(--brand-red)" stroke="#3a0000" stroke-width="1.5"/>
          <path d="M10 4 L25 16 L40 4" fill="none" stroke="#3a0000" stroke-width="1.5"/>
          <circle cx="7" cy="14" r="5.5" fill="none" stroke="var(--ink)" stroke-width="2"/>
          <circle cx="7" cy="14" r="2" fill="none" stroke="var(--ink)" stroke-width="1.6"/>
        </svg>
        <span>dtvickers@krtalentcollective.example</span>
      </li>
      <li class="contact contact--phone">
        <svg class="contact__icon" width="20" height="28" viewBox="0 0 20 28" aria-hidden="true">
          <path d="M6 2 C2 4 1 9 3 15 C5 21 9 26 14 26 L17 21 L12 18 L10 20 C8 18 6 13 7 9 L10 8 L9 2 Z" fill="var(--brand-red)" stroke="#3a0000" stroke-width="1"/>
        </svg>
        <span>555-804-2917</span>
      </li>
      <li class="contact contact--web">
        <svg class="contact__icon" width="36" height="28" viewBox="0 0 36 28" aria-hidden="true">
          <circle cx="13" cy="12" r="8" fill="none" stroke="var(--brand-red)" stroke-width="3.5"/>
          <line x1="19" y1="18" x2="30" y2="26" stroke="var(--ink)" stroke-width="4.5" stroke-linecap="round"/>
        </svg>
        <span>www.krtalentcollective.example</span>
      </li>
    </ul>
  </section>

</main>
</body>
</html>
```